Flyer design for webdesign company

create a flyer that can be printed or sent as an email. The flyer needs to be professional, modern and engaging.

Reason: opportunity for all designers to get their designs in.

Target Market(s)

business owners that do not have a website

Industry/Entity Type

It Company

Font styles to use
Sans Serif

```html
<!DOCTYPE html>
<html lang="en">
<head>
<meta charset="utf-8">
<title>brightsites – Web Design Flyer</title>
<link href="https://fonts.googleapis.com/css2?family=Anton&family=Open+Sans:wght@300;400;700&display=swap" rel="stylesheet">
<style>
  :root{
    --orange:#f7941d;
    --grey:#6d6e71;
    --ink:#1d1d1d;
    --white:#ffffff;
    --backdrop:#3a3a3c;
  }
  *{margin:0;padding:0;box-sizing:border-box}
  html,body{width:953px;height:1200px;overflow:hidden;background:var(--backdrop)}
  .flyer{position:absolute;left:60px;top:66px;width:822px;height:1064px;background:var(--white);overflow:hidden;font-family:"Open Sans",sans-serif}
  .brand{position:absolute;left:36px;top:180px;display:flex;align-items:center;gap:10px}
  .brand-dot{width:34px;height:34px;border-radius:50%;background:var(--grey)}
  .brand-name{font-family:"Open Sans",sans-serif;font-weight:400;font-size:34px;color:var(--orange);letter-spacing:.5px}
  .headline{position:absolute;right:42px;top:30px;text-align:right;font-weight:300;font-size:44px;line-height:52px;color:var(--orange)}
  .rule{position:absolute;left:286px;top:211px;width:498px;height:13px;background:var(--grey)}
  .team-photo{position:absolute;left:168px;top:234px;width:654px;height:463px;background:linear-gradient(100deg,#f4f4f4 0%,#c9ccd2 35%,#2e2f34 55%,#dfe3ea 80%,#f7f7f7 100%)}
  .daily-price{position:absolute;left:52px;top:282px;width:170px;text-align:center;font-family:"Anton",sans-serif;color:var(--orange);font-size:58px;line-height:64px;text-shadow:2px 2px 3px rgba(0,0,0,.35)}
  .call-label{position:absolute;left:48px;top:558px;font-weight:300;font-size:44px;color:var(--orange);letter-spacing:1px}
  .call-number{position:absolute;left:46px;top:614px;font-family:"Anton",sans-serif;font-size:58px;color:var(--orange);text-shadow:2px 2px 3px rgba(0,0,0,.4)}
  .offer-band{position:absolute;left:0;top:697px;width:822px;height:367px;background:var(--orange)}
  .pitch{position:absolute;left:36px;top:10px;font-size:24px;line-height:30px;color:var(--ink)}
  .benefits{position:absolute;left:36px;top:84px;list-style:none}
  .benefits li{display:flex;align-items:center;height:31.3px;font-size:15.5px;color:var(--white)}
  .benefits svg{width:20px;height:18px;margin-right:18px;flex:none}
  .site-url{position:absolute;left:28px;top:312px;font-weight:700;font-size:27px;color:var(--white);letter-spacing:.5px;text-shadow:2px 2px 3px rgba(0,0,0,.45)}
  .price-badge{position:absolute;left:504px;top:31px;width:300px;height:300px}
  .price-text{position:absolute;left:504px;top:31px;width:300px;text-align:center}
  .price-title{margin-top:51px;font-size:35px;font-weight:400;color:var(--ink);font-family:"Open Sans",sans-serif;letter-spacing:.5px}
  .price-amount{font-family:"Anton",sans-serif;font-size:42px;line-height:46px;color:var(--orange);margin-top:2px}
  .price-note{font-size:20px;line-height:26px;color:var(--ink);margin-top:6px}
</style>
</head>
<body>
<main class="flyer">
  <div class="brand"><span class="brand-dot"></span><span class="brand-name">brightsites</span></div>
  <h1 class="headline">ATTRACT MORE<br>CUSTOMERS<br>MAKE MORE MONEY</h1>
  <div class="rule"></div>

  <div class="team-photo" role="img" aria-label="Photo of four smiling business professionals in suits standing together"></div>

  <p class="daily-price">ONLY<br>$3<br>A DAY</p>
  <p class="call-label">CALL TODAY</p>
  <p class="call-number">1-800-555-0147</p>

  <section class="offer-band">
    <p class="pitch">stop wasting money<br>on mailers and print advertising</p>
    <ul class="benefits">
      <li><svg viewBox="0 0 20 18"><path d="M2 10 L7 15 L18 2" fill="none" stroke="#1d1d1d" stroke-width="3"/></svg>97% of people look online for businesses. You need a website</li>
      <li><svg viewBox="0 0 20 18"><path d="M2 10 L7 15 L18 2" fill="none" stroke="#1d1d1d" stroke-width="3"/></svg>You’re losing many customers by not having a website</li>
      <li><svg viewBox="0 0 20 18"><path d="M2 10 L7 15 L18 2" fill="none" stroke="#1d1d1d" stroke-width="3"/></svg>Beat your competition with better visibility and credibility</li>
      <li><svg viewBox="0 0 20 18"><path d="M2 10 L7 15 L18 2" fill="none" stroke="#1d1d1d" stroke-width="3"/></svg>Beautiful websites available now</li>
      <li><svg viewBox="0 0 20 18"><path d="M2 10 L7 15 L18 2" fill="none" stroke="#1d1d1d" stroke-width="3"/></svg>Smart, clean website designs ($3000 value. No extra charge)</li>
      <li><svg viewBox="0 0 20 18"><path d="M2 10 L7 15 L18 2" fill="none" stroke="#1d1d1d" stroke-width="3"/></svg>limited to only 4 websites per area.Don’t miss out!</li>
      <li><svg viewBox="0 0 20 18"><path d="M2 10 L7 15 L18 2" fill="none" stroke="#1d1d1d" stroke-width="3"/></svg>Social media setupoptions (search &amp; social)</li>
    </ul>
    <p class="site-url">www.brightsites-web.com</p>

    <svg class="price-badge" viewBox="0 0 300 300">
      <defs>
        <radialGradient id="badgeFace" cx="45%" cy="35%" r="70%">
          <stop offset="0" stop-color="#ffffff"/>
          <stop offset="0.75" stop-color="#f6f6f6"/>
          <stop offset="1" stop-color="#d8d8d8"/>
        </radialGradient>
      </defs>
      <circle cx="150" cy="150" r="149" fill="#e07f12"/>
      <circle cx="150" cy="150" r="141" fill="#1d1d1d"/>
      <circle cx="150" cy="150" r="136" fill="url(#badgeFace)"/>
    </svg>
    <div class="price-text">
      <p class="price-title">PRICING</p>
      <p class="price-amount">ONLY $99<br>/ MONTH</p>
      <p class="price-note">(That’s $3.30/Day)<br>(No other costs)</p>
    </div>
  </section>
</main>
</body>
</html>
```